Dental Specialist Needs a Business Card

We are a state of the art dental specialty office and need a business card that looks modern but professional.
I have provided our logo design in both vertical and horizontal. We use the design on letterhead in the vertical format but provided both forms for you. Thanks

Please add the address, phone and fax numbers I listed to all designs and please leave a space for website and for my employee name on each design. Thanks 2847 Halloway Avenue, Suite K East Marlow, NY 14391 Phone (716)382-9157 Fax:(716)382-9150 My name is Miles R.Dunford,D.D.S. If you want to show it with my name but the design needs to allow for the name to be switched.

Industry/Entity Type

Business

```html
<!DOCTYPE html>
<html lang="en">
<head>
<meta charset="utf-8">
<title>Keystone Endodontics P.C. — Business Card</title>
<link rel="stylesheet" href="https://fonts.googleapis.com/css2?family=Didact+Gothic&display=swap">
<style>
  :root {
    --paper: #ffffff;
    --brand-blue: #4aa3db;
    --brand-green: #8dc63f;
    --rule-grey: #b5b5b5;
    --ink-dark: #1f1f1f;
  }
  html, body {
    margin: 0;
    padding: 0;
    width: 1200px;
    height: 686px;
    overflow: hidden;
    background: var(--paper);
  }
  .card {
    position: relative;
    width: 1200px;
    height: 686px;
    background: var(--paper);
    overflow: hidden;
    font-family: "Didact Gothic", "Century Gothic", sans-serif;
    font-weight: 400;
  }
  .brand__dot {
    position: absolute;
    left: 198px;
    top: 230px;
    width: 120px;
    height: 120px;
    border-radius: 50%;
    background: var(--brand-green);
  }
  .brand__wordmark {
    position: absolute;
    left: 86px;
    top: 474px;
    width: 344px;
    text-align: center;
    color: var(--ink-dark);
  }
  .brand__rule {
    height: 1px;
    background: var(--rule-grey);
  }
  .brand__name {
    margin: 0;
    padding: 14px 0 12px;
    font-size: 50px;
    font-weight: 400;
    letter-spacing: 6px;
    line-height: 1;
    text-transform: uppercase;
  }
  .brand__suffix {
    margin: 12px 0 0;
    font-size: 25px;
    font-weight: 400;
    letter-spacing: 6px;
    line-height: 1;
    text-transform: uppercase;
  }
  .divider {
    position: absolute;
    left: 471px;
    top: 261px;
    width: 1px;
    height: 338px;
    background: var(--rule-grey);
  }
  .contact {
    position: absolute;
    left: 516px;
    top: 183px;
  }
  .contact__name {
    margin: 0;
    color: var(--brand-blue);
    font-size: 43px;
    font-weight: 400;
    line-height: 50px;
  }
  .contact__credential {
    margin: 0;
    color: var(--brand-blue);
    font-size: 36px;
    line-height: 50px;
    opacity: 0.85;
  }
  .contact__address,
  .contact__lines {
    margin: 0;
    color: var(--brand-green);
    font-size: 38px;
    line-height: 50px;
    font-style: normal;
  }
  .contact__address { margin-top: 14px; }
  .contact__lines { margin-top: 16px; list-style: none; padding: 0; }
</style>
</head>
<body>
  <div class="card">
    <div class="brand">
      <div class="brand__dot"></div>
      <div class="brand__wordmark">
        <div class="brand__rule"></div>
        <p class="brand__name">Keystone</p>
        <div class="brand__rule"></div>
        <p class="brand__suffix">Endodontics P.C.</p>
      </div>
    </div>

    <div class="divider"></div>

    <div class="contact">
      <h1 class="contact__name">Miles R. Dunford</h1>
      <p class="contact__credential">D.D.S.</p>
      <address class="contact__address">2847 Halloway Avenue, Suite K<br>East Marlow, NY 14391</address>
      <ul class="contact__lines">
        <li>P: (716)382-9157</li>
        <li>F: (716)382-9150</li>
        <li>keystoneendo.com</li>
      </ul>
    </div>
  </div>
</body>
</html>
```